Silver Heron Construction Services

Create a business card for my business consulting company
Danielle Vesk, Founder and CEO
4816 Alder Brook Way, Ste 100
Denver, CO. 80451
303.782.4190 cell
dvesk@silverheronconst.example
www.silverheronconst.example

Target Market(s)

Private Equity and Construction Companies

Industry/Entity Type

Business / Sales Consulting

Contact Information for Business Card

Tag Line that says "Where The Road To Success Is Always Under Construction"

Requirements
Must have
• Logo on both sides of the card.
Nice to have
• Add tagline to the same side of the card as my name and contact info

```html
<!DOCTYPE html>
<html lang="en">
<head>
<meta charset="utf-8">
<title>Silver Heron Construction Services – Business Card</title>
<link href="https://fonts.googleapis.com/css2?family=Montserrat:wght@400;500;600&display=swap" rel="stylesheet">
<style>
  :root {
    --backdrop: #ababab;
    --card-light: #ffffff;
    --card-dark: #141414;
    --pattern-dark: #1c1c1c;
    --ink: #111111;
    --muted: #6b6b6b;
    --rule: #9a9a9a;
    --paper: #ffffff;
  }
  * { margin: 0; padding: 0; box-sizing: border-box; }
  html, body {
    width: 1200px; height: 1000px; overflow: hidden;
    background: var(--backdrop);
    font-family: "Montserrat", sans-serif;
  }
  .card {
    position: absolute;
    width: 613px; height: 352px;
    border-radius: 22px;
    overflow: hidden;
  }
  .card--front { left: 292px; top: 126px; background: var(--card-light); }
  .card--back { left: 294px; top: 529px; background: var(--card-dark); }

  .brand-block {
    position: absolute; left: 40px; top: 140px; width: 256px;
    text-align: center; color: var(--ink);
  }
  .brand-name {
    font-weight: 600; font-size: 22px; letter-spacing: 0.5px; line-height: 1.15;
  }
  .brand-name span { display: block; font-size: 10px; letter-spacing: 2px; margin-top: 4px; }
  .tagline {
    position: absolute; left: 40px; top: 244px; width: 256px;
    text-align: center; color: var(--ink);
    font-size: 12.5px; font-weight: 500; letter-spacing: 1.4px; line-height: 16px;
  }
  .divider {
    position: absolute; left: 310px; top: 88px; width: 1px; height: 187px;
    background: var(--rule);
  }
  .contact {
    position: absolute; left: 320px; top: 97px; width: 278px;
    text-align: center;
  }
  .contact__name { font-size: 23px; font-weight: 500; color: var(--ink); line-height: 30px; }
  .contact__title {
    font-size: 10px; letter-spacing: 2.4px; color: var(--muted);
    margin-top: 5px; text-transform: uppercase;
  }
  .contact__icons { display: flex; justify-content: center; gap: 5px; margin-top: 13px; }
  .contact__icons svg { width: 26px; height: 26px; }
  .contact__phone { font-size: 16px; color: var(--muted); letter-spacing: 0.8px; margin-top: 13px; line-height: 20px; }
  .contact__line { font-size: 14px; color: var(--muted); line-height: 20px; }

  .back-pattern {
    position: absolute; inset: 0;
    background: linear-gradient(90deg, var(--pattern-dark), var(--card-dark) 60%, #0d0d0d);
  }
  .back-brand {
    position: absolute; left: 0; right: 0; top: 162px;
    text-align: center; color: var(--paper);
    font-weight: 600; font-size: 13px; letter-spacing: 0.4px; line-height: 1.2;
  }
  .back-brand span { display: block; font-size: 6.5px; letter-spacing: 1px; }
</style>
</head>
<body>
  <section class="card card--front">
    <div class="brand-block">
      <div class="brand-name">SILVER HERON<span>CONSTRUCTION SERVICES</span></div>
    </div>
    <p class="tagline">THE ROAD TO SUCCESS IS<br>ALWAYS UNDER CONSTRUCTION</p>
    <div class="divider"></div>
    <div class="contact">
      <h1 class="contact__name">Danielle Vesk</h1>
      <p class="contact__title">Founder and CEO</p>
      <div class="contact__icons">
        <svg viewBox="0 0 26 26" aria-label="Phone"><circle cx="13" cy="13" r="13" fill="#111"/><path d="M9.6 7.5l1.8 2.6-1 1.2c.7 1.6 1.9 2.8 3.4 3.5l1.2-1 2.6 1.8-.8 1.9c-4.3-.4-8.3-4.4-8.7-8.7z" fill="#fff"/></svg>
        <svg viewBox="0 0 26 26" aria-label="Email"><circle cx="13" cy="13" r="13" fill="#111"/><rect x="7.5" y="9" width="11" height="8" fill="none" stroke="#fff" stroke-width="1.3"/><path d="M7.5 9l5.5 4.5L18.5 9" fill="none" stroke="#fff" stroke-width="1.3"/></svg>
        <svg viewBox="0 0 26 26" aria-label="Location"><circle cx="13" cy="13" r="13" fill="#111"/><path d="M13 6.8a4.2 4.2 0 0 0-4.2 4.2c0 3.1 4.2 8 4.2 8s4.2-4.9 4.2-8A4.2 4.2 0 0 0 13 6.8z" fill="#fff"/><circle cx="13" cy="11" r="1.5" fill="#111"/></svg>
      </div>
      <p class="contact__phone">303-782-4190</p>
      <p class="contact__line">dvesk@silverheronconst.example</p>
      <p class="contact__line">4816 Alder Brook Way, Ste 100</p>
      <p class="contact__line">Denver, CO. 80451</p>
    </div>
  </section>

  <section class="card card--back">
    <div class="back-pattern" role="img" aria-label="Faint repeating brand pattern across the dark card back"></div>
    <div class="back-brand">SILVER HERON<span>CONSTRUCTION SERVICES</span></div>
  </section>
</body>
</html>
```